Vehicle graphics for healthcare company (bluecrestcare.co.uk)

I have a plain white van that needs some branding. I don't mind leaving a bit of the white, so I would consider a half wrap, or large panels of non-white, but I'm open to suggestion.

For a non-wrap design, I happened to see the KDO Van (attached photo), which I thought was a nice clear design. I thought maybe some elements of this could be included. Maybe their large A could be the S of my Blue Crest logo.

The only two colours the company has used to date are the green and grey of the logo. 1B7F8C and 58585A.

The core business we provide is assessment for people about to purchase a wheelchair. We take their measurements, look at their clinical needs and then recommend a product for them to purchase.

The information we need on it:
- our logo (attached)
- Private Wheelchair Assessment
- Occupational Therapy
- Wheelchair Skills

Our contact details to be included:
- www.bluecrestcare.co.uk
- info@bluecrestcare.co.uk
- 02937 418205

Target Market(s)

Wheelchair users and other healthcare providers.

Industry/Entity Type

Healthcare

Font styles to use
Other font styles liked:
• Arthaus Medium

Requirements
Must have
• Logo, contact details. Green/grey colours. 1B7F8C and 58585A
Nice to have
• See attached van, I thought this was a simple, clear design.
Should not have
• Clutter.

```html
<!DOCTYPE html>
<html lang="en">
<head>
<meta charset="utf-8">
<title>Blue Crest Therapy – Van Side Panel</title>
<link href="https://fonts.googleapis.com/css2?family=Saira+Condensed:wght@500;600&family=Poppins:wght@400&display=swap" rel="stylesheet">
<style>
  :root {
    --teal-deep: #0b4f5b;
    --teal-mid: #0d6472;
    --teal-brand: #1b7f8c;
    --teal-bright: #1597a8;
    --grey-brand: #58585a;
    --white: #ffffff;
    --paper: #f4f5f5;
  }
  html, body {
    margin: 0;
    padding: 0;
    width: 1200px;
    height: 682px;
    overflow: hidden;
    background: var(--white);
  }
  .canvas {
    position: relative;
    width: 1200px;
    height: 682px;
    overflow: hidden;
  }
  .panel {
    position: absolute;
    left: 40px;
    top: 105px;
    width: 1100px;
    height: 385px;
    border-radius: 60px 24px 18px 40px;
    overflow: hidden;
    background: var(--white);
    box-shadow: 0 0 0 1px #e3e6e6;
  }
  .panel-art {
    position: absolute;
    inset: 0;
  }
  .photo-area {
    position: absolute;
    left: 285px;
    top: 155px;
    width: 320px;
    height: 230px;
    background: linear-gradient(160deg, #e9ecec 0%, #d8dcdc 55%, #c9cfcf 100%);
  }
  .fern-area {
    position: absolute;
    left: 520px;
    top: 0;
    width: 290px;
    height: 385px;
    background: radial-gradient(ellipse at 30% 75%, var(--teal-deep) 0%, var(--teal-deep) 45%, var(--teal-bright) 70%, rgba(21,151,168,0) 72%);
  }
  .brand {
    position: absolute;
    left: 75px;
    top: 205px;
    display: flex;
    align-items: center;
    gap: 12px;
  }
  .brand-dot {
    width: 18px;
    height: 18px;
    border-radius: 50%;
    background: var(--teal-brand);
  }
  .brand-name {
    font-family: "Saira Condensed", sans-serif;
    font-weight: 600;
    font-size: 50px;
    line-height: 1;
    letter-spacing: 1px;
    color: var(--teal-brand);
    text-transform: uppercase;
  }
  .services {
    position: absolute;
    left: 745px;
    top: 24px;
    margin: 0;
    padding: 0;
    list-style: none;
  }
  .service {
    display: flex;
    align-items: flex-start;
    gap: 16px;
    margin-bottom: 12px;
    font-family: "Saira Condensed", sans-serif;
    font-weight: 500;
    font-size: 27px;
    line-height: 29px;
    color: var(--white);
  }
  .service-icon {
    flex: none;
    width: 34px;
    height: 34px;
    margin-top: -2px;
  }
  .contacts {
    position: absolute;
    left: 795px;
    top: 205px;
    margin: 0;
    padding: 0;
    list-style: none;
    font-family: "Poppins", sans-serif;
    font-size: 15px;
    color: var(--white);
  }
  .contact {
    display: flex;
    align-items: center;
    gap: 14px;
    height: 25px;
  }
  .contact-icon {
    width: 13px;
    height: 13px;
    flex: none;
  }
</style>
</head>
<body>
<main class="canvas">
  <section class="panel">
    <svg class="panel-art" width="1100" height="385" viewBox="0 0 1100 385" aria-hidden="true">
      <path d="M650 0 H1100 V385 H690 C740 300 760 200 720 120 C700 70 670 30 650 0 Z" fill="var(--teal-deep)"/>
      <path d="M760 262 C880 235 980 240 1100 215 V245 C990 268 880 262 790 285 Z" fill="var(--teal-bright)"/>
    </svg>

    <div class="photo-area" role="img" aria-label="Photo of a therapist gently supporting a client's head and shoulder during a treatment session"></div>
    <div class="fern-area" role="img" aria-label="Large decorative teal fern frond sweeping across the panel"></div>

    <div class="brand">
      <span class="brand-dot"></span>
      <span class="brand-name">Blue Crest Therapy</span>
    </div>

    <ul class="services">
      <li class="service">
        <svg class="service-icon" viewBox="0 0 34 34"><circle cx="17" cy="17" r="17" fill="var(--teal-brand)"/><circle cx="17" cy="9" r="2.3" fill="#fff"/><path d="M16 12 v7 h5 l2 5" stroke="#fff" stroke-width="2" fill="none" stroke-linecap="round"/><path d="M13 17 a5.5 5.5 0 1 0 8 6" stroke="#fff" stroke-width="2" fill="none"/></svg>
        <span>Private Wheelchair<br>Assessment</span>
      </li>
      <li class="service">
        <svg class="service-icon" viewBox="0 0 34 34"><circle cx="17" cy="17" r="17" fill="var(--teal-brand)"/><circle cx="19" cy="9" r="2.3" fill="#fff"/><path d="M18 12 v6 h5 M11 16 l7 1" stroke="#fff" stroke-width="2" fill="none" stroke-linecap="round"/><circle cx="15" cy="23" r="5" stroke="#fff" stroke-width="1.8" fill="none"/></svg>
        <span>Occupational Therapy</span>
      </li>
      <li class="service">
        <svg class="service-icon" viewBox="0 0 34 34"><circle cx="17" cy="17" r="17" fill="var(--teal-brand)"/><circle cx="17" cy="9" r="2.3" fill="#fff"/><path d="M16 12 v7 h5 l2 5" stroke="#fff" stroke-width="2" fill="none" stroke-linecap="round"/><path d="M13 17 a5.5 5.5 0 1 0 8 6" stroke="#fff" stroke-width="2" fill="none"/></svg>
        <span>Wheelchair Skills</span>
      </li>
    </ul>

    <ul class="contacts">
      <li class="contact">
        <svg class="contact-icon" viewBox="0 0 13 13"><path d="M2.5 1 l2.3 2.5 -1.2 1.5 c.8 1.7 2 2.9 3.7 3.7 l1.5 -1.2 2.5 2.3 -1.4 1.7 C5.5 11.2 1.8 7.5 .8 2.4 Z" fill="#fff"/></svg>
        <span>02937 418205</span>
      </li>
      <li class="contact">
        <svg class="contact-icon" viewBox="0 0 13 13"><rect x="0.5" y="2.5" width="12" height="8" fill="#fff"/><path d="M0.5 2.5 L6.5 7 L12.5 2.5" stroke="var(--teal-deep)" stroke-width="1.2" fill="none"/></svg>
        <span>info@bluecrestcare.co.uk</span>
      </li>
      <li class="contact">
        <svg class="contact-icon" viewBox="0 0 13 13"><circle cx="6.5" cy="6.5" r="5.5" fill="#fff"/><path d="M1.5 6.5 H11.5 M6.5 1 C4 4 4 9 6.5 12 M6.5 1 C9 4 9 9 6.5 12" stroke="var(--teal-deep)" stroke-width="1" fill="none"/></svg>
        <span>www.bluecrestcare.co.uk</span>
      </li>
    </ul>
  </section>
</main>
</body>
</html>
```